Pick Our Rooftop lead generation web-site.

A Multi-purpose lead generation site with unique selling proposition, hero shot, benefits, social proof, and call-to-action. looking for a clean, modern site that is scalable. The site should be search engine optimized.
Updates

Reason: Will be reviewing designs submitted and ask for changes if any.

Target Market(s)

Homeowner and automobile owners that also own busineses.

Industry/Entity Type

Insurance

Coding

Coded - Design and coding required

Number of Pages Required

5+ page

Font styles to use
Serif

Requirements
Must have
• Optimization for mobile devices, a clean site similar to (https://shieldbramble.com), Easy to use, Interactivity, and easy content management. Quote forms for personal and commercial auto, homeowners, business owners insurance. Adroll on pages (analytics)
Nice to have
• Uses of Technology similar to https://protavo.com. Integration or ability to push to third-party tools. Auto email responses, Chat integration, social media (join our group, sign up RSS feeds).
Should not have
• Links that closes our site.

```html
<!DOCTYPE html>
<html lang="en">
<head>
<meta charset="utf-8">
<title>Pick Our Rooftop – Home Insurance Quotes</title>
<link href="https://fonts.googleapis.com/css2?family=Montserrat:wght@300;400;500;600&family=Open+Sans:wght@400;600&display=swap" rel="stylesheet">
<style>
:root{
  --blue:#1b7cc6;
  --blue-dark:#135f9b;
  --hero-bg:#def1f8;
  --panel:#7db9e0;
  --navy:#1d3146;
  --text:#6d6d6d;
  --heading:#1b6fb0;
  --line:#d9d9d9;
  --footer-band:#eeeeee;
  --white:#ffffff;
}
*{box-sizing:border-box;margin:0;padding:0}
html,body{width:1200px;height:2416px;overflow:hidden;background:var(--white)}
body{font-family:"Open Sans",Arial,sans-serif;color:var(--text);position:relative}
h1,h2,h3{font-family:"Montserrat",Arial,sans-serif;font-weight:400}

/* header */
.site-header{position:absolute;top:0;left:0;width:1200px;height:88px;display:flex;align-items:center;justify-content:space-between;padding:0 116px 0 160px;background:var(--white)}
.brand{display:flex;align-items:center;gap:12px;font-family:"Montserrat",sans-serif;font-weight:600;font-size:22px;color:var(--blue-dark)}
.brand-square{width:30px;height:30px;background:var(--blue)}
.menu{display:flex;align-items:center;gap:12px;font-size:14px;color:#555}
.menu-btn{width:40px;height:32px;background:var(--blue);display:flex;flex-direction:column;justify-content:center;align-items:center;gap:4px}
.menu-btn span{display:block;width:18px;height:2px;background:var(--white)}

/* hero */
.hero{position:absolute;top:88px;left:0;width:1200px;height:472px;background:linear-gradient(180deg,#e9f7fb,var(--hero-bg))}
.hero-art{position:absolute;left:80px;top:32px;width:420px;height:420px;border-radius:6px;background:radial-gradient(circle at 50% 55%,#f3e9d4 0%,#cfe3ee 55%,#def1f8 80%)}
.quote-title{position:absolute;left:520px;top:74px;font-family:"Montserrat",sans-serif;font-weight:600;font-size:22px;color:var(--blue)}
.quote-sub{position:absolute;left:520px;top:110px;font-size:14px;color:#6a8fa6}
.quote-form{position:absolute;left:520px;top:132px;width:620px;height:320px;background:var(--panel);padding:34px 36px;display:grid;grid-template-columns:1fr 1fr;gap:26px 30px;align-content:start}
.field{height:44px;border-bottom:1px solid rgba(255,255,255,.7);color:rgba(255,255,255,.9);font-size:14px;padding-top:14px}
.form-actions{grid-column:1/3;display:flex;align-items:center;gap:22px;margin-top:20px}
.btn{display:inline-block;background:var(--blue);color:var(--white);font-family:"Montserrat",sans-serif;font-size:14px;font-weight:500;padding:12px 40px}
.form-note{color:var(--white);font-size:13px}

/* welcome */
.welcome{position:absolute;top:560px;left:0;width:1200px;height:420px;text-align:center;padding-top:80px}
.section-title{font-size:40px;color:var(--heading)}
.title-rule{width:70px;height:2px;background:var(--blue);margin:18px auto 30px}
.welcome p{width:900px;margin:0 auto;font-size:15px;line-height:28px}
.welcome .btn{margin-top:36px;padding:12px 44px}

/* split sections */
.split{position:absolute;left:0;width:1200px;height:420px}
.benefits{top:980px;border-top:1px solid var(--line)}
.features{top:1400px;height:400px}
.photo{position:absolute;top:0;height:100%}
.benefits .photo{left:0;width:592px;background:linear-gradient(160deg,#9aa8b6,#5e6e7e 50%,#3d4a3f)}
.features .photo{left:592px;width:608px;background:linear-gradient(170deg,#9fc3e6 0%,#d9c8a8 45%,#8a7a5e 75%,#4d6b3c)}
.split-text{position:absolute;top:64px;width:500px}
.benefits .split-text{left:620px;width:480px}
.features .split-text{left:110px;width:440px}
.split-text h2{font-size:34px;color:var(--heading)}
.split-text .title-rule{margin:14px 0 26px}
.point{display:flex;gap:16px;margin-bottom:22px;font-size:14px;line-height:24px}
.point svg{flex:none;margin-top:5px}

/* testimonials */
.testimonials{position:absolute;top:1800px;left:0;width:1200px;height:460px;background:linear-gradient(180deg,#2a4462,var(--navy) 60%,#15263a);color:var(--white)}
.testimonials h2{text-align:center;padding-top:56px;font-size:34px;color:var(--white)}
.testimonials .title-rule{background:var(--white);margin:14px auto 30px}
.cards{display:flex;justify-content:center;gap:110px}
.card{width:390px;display:grid;grid-template-columns:120px 1fr;gap:0 22px}
.card-side{display:flex;flex-direction:column;gap:12px}
.avatar{width:120px;height:132px;border:4px solid var(--white);background:linear-gradient(180deg,#c7cfd6,#8f9ba6)}
.card h3{font-size:24px;margin-top:22px}
.role{font-size:13px;opacity:.8;margin-top:4px}
.quote-mark{display:block;font-family:"Montserrat",sans-serif;font-size:36px;line-height:1;margin-top:14px;height:24px}
.card-body{font-size:13px;line-height:21px}
.badges{display:flex;gap:8px;align-items:center}
.badge{width:56px;height:26px;background:rgba(255,255,255,.85);border-radius:4px}
.badge.rating{width:56px;height:12px;background:#d0392b;border-radius:2px}
.arrow{position:absolute;top:250px;width:30px;height:30px}
.arrow.prev{left:70px}.arrow.next{right:70px}

/* footer */
.site-footer{position:absolute;top:2260px;left:0;width:1200px;height:90px;display:flex;align-items:center;justify-content:space-between;padding:0 116px 0 160px;border-bottom:1px solid var(--line)}
.copyright{font-size:13px;color:#444;margin-left:-190px}
.review{display:flex;align-items:center;gap:10px;font-size:13px;color:#444}
.review i{display:block;width:18px;height:18px;border-radius:50%;background:#c9c9c9}
.review i.accent{background:#d0392b}
.disclaimer{position:absolute;top:2350px;left:0;width:1200px;height:66px;background:var(--footer-band);padding:16px 160px;font-size:11px;line-height:17px;color:#777}
.disclaimer strong{color:#444}
</style>
</head>
<body>

<header class="site-header">
  <div class="brand"><span class="brand-square"></span>Pick Our Rooftop</div>
  <div class="menu">Menu <span class="menu-btn"><span></span><span></span><span></span></span></div>
</header>

<section class="hero">
  <div class="hero-art" role="img" aria-label="Illustration of a smiling homeowner standing in front of a two-storey house"></div>
  <h2 class="quote-title">Get The Quote Pick Our Rooftop</h2>
  <p class="quote-sub">Compare trusted home insurance quotes in minutes and save more today.</p>
  <form class="quote-form">
    <div class="field">Full Name</div>
    <div class="field">Phone Number</div>
    <div class="field">Email Address</div>
    <div class="field">Zip Code</div>
    <div class="form-actions"><span class="btn">Submit</span><span class="form-note">We respect your privacy</span></div>
  </form>
</section>

<section class="welcome">
  <h1 class="section-title">Welcome To Pick Our Rooftop</h1>
  <div class="title-rule"></div>
  <p>We help homeowners, drivers and business owners find the right protection at the right price. Tell us a little about your home and we compare plans from dependable carriers, so you can review clear options side by side. No pressure, no hidden fees, just honest answers from people who care about keeping your family and property safe every single day of the year.</p>
  <span class="btn">Contact Us</span>
</section>

<section class="split benefits">
  <div class="photo" role="img" aria-label="Photo of a modern house entrance with a person at the door"></div>
  <div class="split-text">
    <h2>Benefits</h2>
    <div class="title-rule"></div>
    <div class="point"><svg width="14" height="14" viewBox="0 0 14 14"><path d="M2 7h9M7 3l4 4-4 4" stroke="#1b7cc6" stroke-width="2" fill="none"/></svg><p>Get quotes from several top rated insurers with one short form, and see coverage, deductibles and monthly costs laid out clearly on one page.</p></div>
    <div class="point"><svg width="14" height="14" viewBox="0 0 14 14"><path d="M2 7h9M7 3l4 4-4 4" stroke="#1b7cc6" stroke-width="2" fill="none"/></svg><p>Licensed agents review your answers and suggest discounts you may have missed, from bundled auto policies to new roofs and security systems.</p></div>
    <div class="point"><svg width="14" height="14" viewBox="0 0 14 14"><path d="M2 7h9M7 3l4 4-4 4" stroke="#1b7cc6" stroke-width="2" fill="none"/></svg><p>Switch at your own pace with free support, fast policy documents and friendly reminders before every renewal date comes around.</p></div>
  </div>
</section>

<section class="split features">
  <div class="split-text">
    <h2>Features</h2>
    <div class="title-rule"></div>
    <div class="point"><svg width="14" height="14" viewBox="0 0 14 14"><path d="M2 7h9M7 3l4 4-4 4" stroke="#1b7cc6" stroke-width="2" fill="none"/></svg><p>Coverage for homes, condos and rentals, with options for flood, wind and fire added whenever your needs change over time.</p></div>
    <div class="point"><svg width="14" height="14" viewBox="0 0 14 14"><path d="M2 7h9M7 3l4 4-4 4" stroke="#1b7cc6" stroke-width="2" fill="none"/></svg><p>Commercial auto and business owner plans built for people who run a company from home or keep a small fleet on the road.</p></div>
    <div class="point"><svg width="14" height="14" viewBox="0 0 14 14"><path d="M2 7h9M7 3l4 4-4 4" stroke="#1b7cc6" stroke-width="2" fill="none"/></svg><p>Secure online forms, quick email replies and live chat help whenever you have a question about a quote or a claim.</p></div>
  </div>
  <div class="photo" role="img" aria-label="Photo of a large suburban house with palm trees under a blue sky"></div>
</section>

<section class="testimonials">
  <h2>Customer Testimonials</h2>
  <div class="title-rule"></div>
  <svg class="arrow prev" viewBox="0 0 30 30"><path d="M19 6l-9 9 9 9" stroke="#fff" stroke-width="2" fill="none"/></svg>
  <svg class="arrow next" viewBox="0 0 30 30"><path d="M11 6l9 9-9 9" stroke="#fff" stroke-width="2" fill="none"/></svg>
  <div class="cards">
    <article class="card">
      <div class="card-side">
        <div class="avatar" role="img" aria-label="Portrait photo of customer Daniel Ortiz"></div>
        <div class="badges"><span class="badge"></span><span class="badge rating"></span></div>
      </div>
      <div>
        <h3>Daniel Ortiz</h3><p class="role">Home Owner</p>
        <span class="quote-mark">“</span>
        <p class="card-body">The whole process took ten minutes. I compared four offers, picked the best one and saved almost three hundred dollars on my home policy this year.</p>
      </div>
    </article>
    <article class="card">
      <div class="card-side">
        <div class="avatar" role="img" aria-label="Portrait photo of customer Rafael Lindqvist"></div>
        <div class="badges"><span class="badge"></span><span class="badge rating"></span></div>
      </div>
      <div>
        <h3>Rafael Lindqvist</h3><p class="role">Home Owner</p>
        <span class="quote-mark">“</span>
        <p class="card-body">Their agent found a bundle for my house and work van that I never knew existed. Friendly service and very clear answers every time.</p>
      </div>
    </article>
  </div>
</section>

<footer class="site-footer">
  <div class="brand"><span class="brand-square"></span>Pick Our Rooftop</div>
  <p class="copyright">© 2017 Company Name. | All Rights Reserved</p>
  <div class="review">Review On <i></i><i class="accent"></i><i></i></div>
</footer>
<p class="disclaimer"><strong>Disclaimer:</strong> Pick Our Rooftop is not an insurance company. Quotes shown are estimates only and final rates are set by each carrier after review. Coverage may vary by state and is subject to the terms of every policy issued.</p>

</body>
</html>
```